Software Company Business Card

We are looking for a new design of our business card. The design will also be used in the rest of our branding and marketing materials as we want to keep it all uniform. We sell POS software to fine/luxury jewelers and also offer other business services as well to help the jeweler manage their business and need something more updated, technical and fresh, preferably more on the masculine side. We do not want any designs with gems in them but if possible would like to incorporate the circle and arrow in the logo into the design, but not a requirement if you can't make it work. I would like to see a variety of the mix. The colors need to remain our blue and orange and the logo can not change. The squiggly lines have been used as our corporate identity for over 20 years and its time to update. Our company name is PELK (Bright Ledger Counter Solutions).

Target Market(s)

High End Jewelers

Industry/Entity Type

Software

Contact Information for Business Card

Requirements
Must have
• Our logo and the colors must remain the same. Blue is #d95d39 and Orange is #0f5682.
Nice to have
• The circle and arrow incorporated but not a requirement.
Should not have
• Anything jewelry or gem related.

```html
<!DOCTYPE html>
<html lang="en">
<head>
<meta charset="utf-8">
<title>PELK Business Card</title>
<link rel="stylesheet" href="https://fonts.googleapis.com/css2?family=Open+Sans:wght@400;700;800&display=swap">
<style>
  :root {
    --pelk-blue: #0f5682;
    --pelk-orange: #d95d39;
    --paper: #ffffff;
    --ink: #3a3a3a;
    --backdrop: #cfcfcf;
  }
  * { margin: 0; padding: 0; box-sizing: border-box; }
  html, body { width: 1200px; height: 873px; overflow: hidden; }
  body {
    background: var(--backdrop);
    font-family: "Open Sans", Arial, sans-serif;
    position: relative;
  }
  .card {
    position: absolute;
    top: 288px;
    width: 520px;
    height: 297px;
    overflow: hidden;
    box-shadow: 0 2px 6px rgba(0,0,0,0.18);
  }
  .card-front { left: 65px; background: var(--paper); }
  .card-back { left: 615px; background: var(--pelk-blue); }

  .wordmark {
    position: absolute;
    display: flex;
    align-items: center;
    gap: 8px;
    font-weight: 800;
    letter-spacing: -1px;
    line-height: 1;
  }
  .wordmark-dot { border-radius: 50%; display: block; }
  .card-front .wordmark { left: 46px; top: 46px; font-size: 40px; color: var(--pelk-blue); }
  .card-front .wordmark-dot { width: 40px; height: 40px; background: var(--pelk-orange); }
  .card-back .wordmark { left: 182px; top: 196px; font-size: 50px; color: var(--paper); }
  .card-back .wordmark-dot { width: 52px; height: 52px; background: var(--paper); }

  .person { position: absolute; left: 46px; top: 134px; }
  .person-name { font-size: 16px; font-weight: 700; color: var(--pelk-blue); }
  .person-role { font-size: 12px; color: var(--pelk-orange); line-height: 1.1; }

  .contact-list {
    position: absolute; left: 46px; top: 192px;
    list-style: none; font-size: 11.5px; color: var(--ink); line-height: 15px;
  }
  .contact-list li { display: flex; align-items: center; gap: 6px; }
  .contact-list svg { width: 10px; height: 10px; fill: var(--pelk-blue); flex: none; }
  .note { color: var(--pelk-orange); }

  .address {
    position: absolute; left: 229px; top: 222px;
    font-size: 11.5px; color: var(--ink); line-height: 15px; font-style: normal;
  }
  .address-company { color: var(--pelk-orange); }

  .brand-disc { position: absolute; top: 0; left: 0; }
</style>
</head>
<body>
  <section class="card card-front" aria-label="Business card front">
    <svg class="brand-disc" width="520" height="297" viewBox="0 0 520 297" aria-hidden="true">
      <circle cx="520" cy="149" r="149" fill="var(--pelk-orange)"/>
    </svg>

    <div class="wordmark">PELK <span class="wordmark-dot"></span></div>

    <div class="person">
      <p class="person-name">Dorian Whitfield</p>
      <p class="person-role">Founder</p>
    </div>

    <ul class="contact-list">
      <li><svg viewBox="0 0 10 10"><path d="M2 0.5 L4 2.5 L3 3.6 Q4.2 5.8 6.4 7 L7.5 6 L9.5 8 L8 9.5 Q3 9 0.5 2 Z"/></svg>1-800-555-0142 <span class="note">(Toll Free)</span></li>
      <li><svg viewBox="0 0 10 10"><path d="M2 0.5 L4 2.5 L3 3.6 Q4.2 5.8 6.4 7 L7.5 6 L9.5 8 L8 9.5 Q3 9 0.5 2 Z"/></svg>702-555-0100 <span class="note">(Phone)</span></li>
      <li><svg viewBox="0 0 10 10"><rect x="2.5" y="0.5" width="5" height="3"/><rect x="0.5" y="4" width="9" height="4" rx="1"/><rect x="2.5" y="7" width="5" height="2.5"/></svg>702-555-0126</li>
      <li><svg viewBox="0 0 10 10"><rect x="0.5" y="2" width="9" height="6"/><path d="M0.8 2.3 L5 5.5 L9.2 2.3" stroke="#fff" stroke-width="0.9" fill="none"/></svg>info@pelkusa.com</li>
      <li><svg viewBox="0 0 10 10"><circle cx="5" cy="5" r="4.5"/><path d="M0.5 5 H9.5 M5 0.5 V9.5 M5 0.5 Q2 5 5 9.5 M5 0.5 Q8 5 5 9.5" stroke="#fff" stroke-width="0.6" fill="none"/></svg>www.pelkusa.com</li>
    </ul>

    <address class="address">
      <span class="address-company">PELK USA</span><br>
      P.O. Box 41208<br>
      Carson Ridge, NV 89011 USA
    </address>
  </section>

  <section class="card card-back" aria-label="Business card back">
    <svg class="brand-disc" width="520" height="297" viewBox="0 0 520 297" aria-hidden="true">
      <circle cx="0" cy="149" r="168" fill="var(--paper)"/>
      <circle cx="0" cy="149" r="149" fill="var(--pelk-orange)"/>
    </svg>
    <div class="wordmark">PELK <span class="wordmark-dot"></span></div>
  </section>
</body>
</html>
```